Riverbend City (by the numbers)

We (city communications office of Riverbend City, Arkansas) are launching a magazine to be delivered to every house in the community. We would like the first inside page to be an infographic of the important and interesting "numbers" from 2017. We want it to be visually interesting and convey the huge amount of important services we provide our residents. I have included a document with the relevant statistics to be used.

Target Market(s)

Residents of our city

Industry/Entity Type

House

Colors

Designer to choose colors to be used in the design.

Requirements
Must have
• Our logo must be prominent. The dimensions should be able to fit onto a standard full page magazine. If the infographic is best displayed on two pages we will accept that as well, and change our layout.
Nice to have
• Not every statistic we have provided must be used but if they can be, that is preferable. I have also included some inspirational infographics that appealed to me and inspired the idea, but I am excited about new concepts that might not look anything like those that I have provided.
Should not have
• The design should not have anything incorporated that cannot be presented to families in our community. It must be all ages friendly.

```html
<!DOCTYPE html>
<html lang="en">
<head>
<meta charset="utf-8">
<title>Riverbend City – 2017 By The Numbers</title>
<link href="https://fonts.googleapis.com/css2?family=Montserrat:wght@400;700;800&display=swap" rel="stylesheet">
<style>
  :root {
    --page-bg: #ffffff;
    --paper: #f7f7ea;
    --ink: #4d4d52;
    --ink-dark: #3a3a3c;
    --city-blue: #1f4ea1;
    --visitor-orange: #e58410;
    --park-green: #5f8a1c;
    --cream: #f2eecb;
    --tire-dark: #35301f;
    --asphalt: #58585c;
    --fire-yellow: #f3c81a;
  }
  * { margin: 0; padding: 0; box-sizing: border-box; }
  html, body { width: 1200px; height: 1000px; overflow: hidden; background: var(--page-bg); }
  body { position: relative; font-family: "Montserrat", sans-serif; color: var(--ink); }

  .infographic-page {
    position: absolute; left: 277px; top: 132px; width: 646px; height: 835px;
    background: var(--paper);
  }
  .infographic-page > * { position: absolute; }

  .city-name {
    left: 40px; top: 46px; width: 120px;
    display: flex; flex-direction: column; align-items: center; gap: 8px;
    color: var(--city-blue); font-weight: 800; font-size: 20px; line-height: 1.05; text-align: center;
  }
  .city-name .mark-dot { width: 22px; height: 22px; border-radius: 50%; background: var(--city-blue); }

  .title-year {
    left: 300px; top: 18px; width: 260px; text-align: center;
    font-weight: 800; font-size: 104px; line-height: 1; letter-spacing: -2px; color: var(--ink);
  }
  .title-sub {
    left: 240px; top: 116px; width: 380px; text-align: center;
    font-weight: 700; font-size: 40px; letter-spacing: -0.5px; color: var(--ink);
  }

  .legend { top: 214px; font-size: 10px; white-space: nowrap; display: flex; align-items: center; gap: 2px; }
  .legend strong { font-weight: 700; }
  .legend .dot { width: 9px; height: 10px; }
  .legend-unit { left: 15px; }
  .legend-population { left: 226px; }
  .legend-visitors { right: 18px; }

  .people-chart { left: 16px; top: 230px; }

  .service-ring { left: 0; top: 470px; }
  .stat-label { font-size: 10px; line-height: 1.2; white-space: nowrap; }
  .stat-label strong { font-weight: 700; display: block; }
  .stat-label.inline strong { display: inline; }
  .stat-tires { left: 313px; top: 502px; }
  .stat-garbage { left: 313px; top: 566px; }
  .stat-asphalt { left: 313px; top: 598px; }
  .stat-green { left: 313px; top: 691px; }
  .stat-fire { left: 131px; top: 561px; }
  .stat-police { left: 131px; top: 631px; }

  .parks-label { left: 15px; top: 782px; font-size: 10px; }
  .playground-label { right: 16px; top: 782px; font-size: 10px; }
  .parks-label strong, .playground-label strong { font-weight: 700; }
  .parks-row { left: 15px; top: 798px; }
</style>
</head>
<body>
<main class="infographic-page">
  <div class="city-name"><span class="mark-dot"></span><span>Riverbend City</span></div>
  <h1 class="title-year">2017</h1>
  <h2 class="title-sub">By The Numbers</h2>

  <div class="legend legend-unit">
    <svg class="dot" viewBox="0 0 10 10"><circle cx="5" cy="2.5" r="2.3" fill="var(--ink)"/><path d="M0.5 10 Q0.5 5 5 5 Q9.5 5 9.5 10 Z" fill="var(--ink)"/></svg>
    <span>=1,000 people</span>
  </div>
  <div class="legend legend-population">
    <svg class="dot" viewBox="0 0 10 10"><circle cx="5" cy="2.5" r="2.3" fill="var(--city-blue)"/><path d="M0.5 10 Q0.5 5 5 5 Q9.5 5 9.5 10 Z" fill="var(--city-blue)"/></svg>
    <span><strong>Population</strong> - 65,004</span>
  </div>
  <div class="legend legend-visitors">
    <svg class="dot" viewBox="0 0 10 10"><circle cx="5" cy="2.5" r="2.3" fill="var(--visitor-orange)"/><path d="M0.5 10 Q0.5 5 5 5 Q9.5 5 9.5 10 Z" fill="var(--visitor-orange)"/></svg>
    <span><strong>Visitors to Cedar Bend Park</strong> - 779,621</span>
  </div>

  <svg class="people-chart" width="612" height="228" viewBox="0 0 612 228" role="img" aria-label="Pictograph: population and park visitors in thousands">
    <defs>
      <pattern id="person-blue" width="10.55" height="8.7" patternUnits="userSpaceOnUse">
        <circle cx="5.2" cy="2.2" r="2" fill="var(--city-blue)"/>
        <path d="M1.3 8 Q1.3 4.3 5.2 4.3 Q9.1 4.3 9.1 8 Z" fill="var(--city-blue)"/>
      </pattern>
      <pattern id="person-orange" width="10.55" height="8.7" patternUnits="userSpaceOnUse">
        <circle cx="5.2" cy="2.2" r="2" fill="var(--visitor-orange)"/>
        <path d="M1.3 8 Q1.3 4.3 5.2 4.3 Q9.1 4.3 9.1 8 Z" fill="var(--visitor-orange)"/>
      </pattern>
    </defs>
    <rect x="0" y="0" width="612" height="8.7" fill="url(#person-blue)"/>
    <rect x="0" y="8.7" width="179.35" height="8.7" fill="url(#person-blue)"/>
    <rect x="242.65" y="8.7" width="369.35" height="8.7" fill="url(#person-orange)"/>
    <rect x="0" y="17.4" width="612" height="208.8" fill="url(#person-orange)"/>
  </svg>

  <svg class="service-ring" width="646" height="240" viewBox="0 0 646 240" role="img" aria-label="Ring chart of city services">
    <g transform="translate(131 131) rotate(-90)" fill="none" stroke-width="20">
      <circle r="102" stroke="var(--cream)"/>
      <circle r="102" stroke="var(--tire-dark)" stroke-dasharray="14.2 640.9" stroke-dashoffset="-46.3"/>
      <circle r="102" stroke="var(--visitor-orange)" stroke-dasharray="78.3 640.9" stroke-dashoffset="-67.6"/>
      <circle r="102" stroke="var(--asphalt)" stroke-dasharray="21.4 640.9" stroke-dashoffset="-156.6"/>
      <circle r="102" stroke="var(--park-green)" stroke-dasharray="402.4 640.9" stroke-dashoffset="-270.6"/>
    </g>
    <g stroke-width="1.2">
      <line x1="206" y1="39" x2="308" y2="39" stroke="var(--tire-dark)"/>
      <line x1="240" y1="104" x2="308" y2="104" stroke="var(--visitor-orange)"/>
      <line x1="240" y1="136" x2="308" y2="136" stroke="var(--asphalt)"/>
      <line x1="183" y1="228" x2="308" y2="228" stroke="var(--park-green)"/>
    </g>
    <g transform="translate(68 76)">
      <path d="M0 0 H50 V28 Q50 46 25 56 Q0 46 0 28 Z" fill="var(--fire-yellow)"/>
      <path d="M5 17 H45 V28 Q45 42 25 51 Q5 42 5 28 Z" fill="var(--city-blue)"/>
      <text x="25" y="14" text-anchor="middle" font-family="Montserrat, sans-serif" font-weight="800" font-size="12" fill="#ffffff">FIRE</text>
    </g>
    <g transform="translate(70 146)">
      <path d="M0 0 H50 V28 Q50 46 25 56 Q0 46 0 28 Z" fill="var(--city-blue)"/>
      <path d="M3 3 H47 V28 Q47 43 25 53 Q3 43 3 28 Z" fill="#ffffff"/>
      <path d="M6 18 H44 V28 Q44 41 25 50 Q6 41 6 28 Z" fill="var(--tire-dark)"/>
      <text x="25" y="15" text-anchor="middle" font-family="Montserrat, sans-serif" font-weight="800" font-size="11" fill="var(--city-blue)">POLICE</text>
    </g>
  </svg>

  <p class="stat-label inline stat-tires"><strong>Used Tires Recycled</strong> – 4,221</p>
  <p class="stat-label inline stat-garbage"><strong>Tons of Household Garbage Collected</strong> – 16,768</p>
  <p class="stat-label stat-asphalt"><strong>Tons of Asphalt Used in Repairing Potholes and Street Overlays</strong>5,952</p>
  <p class="stat-label stat-green"><strong>Cubic Yards of Green (Yard) Waste Collected</strong>116,675</p>
  <p class="stat-label stat-fire"><strong>Fire 911 Calls</strong>12,560</p>
  <p class="stat-label stat-police"><strong>Police 911 Calls</strong>26,660</p>

  <p class="parks-label"><strong>Neighborhood Parks</strong> – 34</p>
  <p class="playground-label"><strong>Open Hands Inclusive Playgrounds Built for Kids with Special Needs</strong> – 1</p>

  <svg class="parks-row" width="616" height="16" viewBox="0 0 616 16" role="img" aria-label="34 neighborhood parks and 1 inclusive playground">
    <defs>
      <g id="park-icon">
        <path d="M1 14 L4 3 L7 14 M9 14 L12 3 L15 14 M4 3 H12" stroke-width="1.6" fill="none"/>
        <rect x="7" y="8" width="3" height="2"/>
      </g>
      <pattern id="park-green" width="17.5" height="16" patternUnits="userSpaceOnUse">
        <use href="#park-icon" stroke="var(--park-green)" fill="var(--park-green)"/>
      </pattern>
    </defs>
    <rect x="0" y="0" width="595" height="16" fill="url(#park-green)"/>
    <use href="#park-icon" x="599" stroke="var(--city-blue)" fill="var(--city-blue)"/>
  </svg>
</main>
</body>
</html>
```